Card design for orthopaedic surgeons working as The Brindlewood Orthopaedic Centre

Business cards, letterhead

Colors

Designer to choose colors to be used in the design.

Requirements
Must have
• Late addition.
• Cards letterhead must have logos of
• Corvane Federated Institute of Surgeons
• Meridale Orthopaedic Society
Nice to have
• Back of card to have space for appointment time to be added by hand and some blank space for writing incidental other notes.

```html
<!DOCTYPE html>
<html lang="en">
<head>
<meta charset="utf-8">
<title>The Brindlewood Orthopaedic Centre – Business Cards</title>
<link rel="stylesheet" href="https://fonts.googleapis.com/css2?family=Open+Sans:wght@400;600;700&display=swap">
<style>
  :root {
    --stage: #1d1e20;
    --card: #ffffff;
    --navy: #0f3551;
    --sky: #35adf5;
    --ink: #1b1b1b;
    --white: #ffffff;
  }
  * { box-sizing: border-box; margin: 0; padding: 0; }
  html, body {
    width: 1200px; height: 960px; overflow: hidden;
    background: var(--stage);
    font-family: "Open Sans", Arial, sans-serif;
  }
  .stage { position: relative; width: 1200px; height: 960px; }
  .card {
    position: absolute; left: 320px;
    width: 560px; height: 320px;
    background: var(--card);
    overflow: hidden;
  }
  .card--back { top: 110px; }
  .card--front { top: 530px; }

  .brand-name {
    font-weight: 400; color: var(--navy);
    letter-spacing: -0.2px; white-space: nowrap;
  }

  /* back */
  .card--back .brand-name {
    position: absolute; top: 108px; left: 0; right: 0;
    text-align: center; font-size: 27px;
  }
  .web-line {
    position: absolute; top: 196px; left: 0; right: 0;
    text-align: center; font-size: 17px; letter-spacing: 4px; color: var(--ink);
  }
  .web-line .web-domain { color: var(--sky); }

  /* front */
  .card--front .brand-name {
    position: absolute; top: 22px; left: 30px; font-size: 21px;
  }
  .person { position: absolute; top: 70px; left: 34px; }
  .person-name { font-weight: 700; font-size: 18px; color: var(--navy); line-height: 1.3; }
  .person-title { font-size: 14px; color: var(--sky); line-height: 1.3; }

  .contact-list {
    position: absolute; top: 124px; left: 34px; list-style: none;
    font-size: 14px; color: var(--ink);
  }
  .contact-list li { display: flex; align-items: center; gap: 8px; height: 22px; }
  .contact-icon { width: 12px; height: 12px; flex: none; }

  .wave { position: absolute; inset: 0; width: 560px; height: 320px; }

  .address {
    position: absolute; right: 26px; bottom: 14px;
    text-align: right; color: var(--white); font-size: 15px; line-height: 1.35;
  }
</style>
</head>
<body>
<main class="stage">

  <section class="card card--back" aria-label="Business card back">
    <p class="brand-name">The Brindlewood Orthopaedic Centre</p>
    <p class="web-line">www.<span class="web-domain">brindlewoodortho</span>.com</p>
  </section>

  <section class="card card--front" aria-label="Business card front">
    <svg class="wave" viewBox="0 0 560 320" aria-hidden="true">
      <path fill="var(--navy)" d="M0,204 C80,250 220,262 340,256 C440,252 510,240 560,230 L560,246 C500,254 420,262 330,264 C210,266 70,258 0,224Z"/>
      <path fill="var(--sky)" d="M0,234 C70,270 210,274 330,272 C430,270 500,262 560,254 L560,320 L0,320Z"/>
    </svg>

    <p class="brand-name">The Brindlewood Orthopaedic Centre</p>

    <div class="person">
      <p class="person-name">Marla Qwinton</p>
      <p class="person-title">Title</p>
    </div>

    <ul class="contact-list">
      <li>
        <svg class="contact-icon" viewBox="0 0 12 12" aria-hidden="true"><circle cx="6" cy="6" r="5.5" fill="none" stroke="var(--sky)"/><path d="M4,3.2 L5,3 L5.6,4.6 L4.9,5.2 C5.3,6 6,6.7 6.8,7.1 L7.4,6.4 L9,7 L8.8,8 C6.5,8.5 3.5,5.5 4,3.2Z" fill="var(--sky)"/></svg>
        <span>012-555-0148</span>
      </li>
      <li>
        <svg class="contact-icon" viewBox="0 0 12 12" aria-hidden="true"><circle cx="6" cy="6" r="5.5" fill="var(--sky)"/><rect x="3" y="4" width="6" height="4.2" fill="var(--white)"/><path d="M3,4 L6,6.4 L9,4" fill="none" stroke="var(--sky)" stroke-width="0.8"/></svg>
        <span>info@brindlewoodortho.com</span>
      </li>
      <li>
        <svg class="contact-icon" viewBox="0 0 12 12" aria-hidden="true"><circle cx="6" cy="6" r="5" fill="none" stroke="var(--sky)" stroke-width="1.2"/><ellipse cx="6" cy="6" rx="2" ry="5" fill="none" stroke="var(--sky)" stroke-width="0.8"/><path d="M1,6 H11" stroke="var(--sky)" stroke-width="0.8"/></svg>
        <span>www.brindlewoodortho.com</span>
      </li>
    </ul>

    <p class="address">Street Name, City Name<br>Zipcode - 012345</p>
  </section>

</main>
</body>
</html>
```